Professional Home Buyer business card needed

I need a pretty straight forward business card designed. We help people that NEED to sell their homes solve problems. We perform all types of Real Estate transactions including flip, wholesale, investment, rental property and multi family. The card will mainly be used to give to prospective Sellers but will also be given to Real Estate Investors as well. It should professional and very easy to read, most clients are older people.

Target Market(s)

Distressed home sellers as well as Real Estate investors

Industry/Entity Type

Real Estate

Contact Information for Business Card

should be a professional layout

Colors
ec1f27
ffffff
000000

Requirements
Must have
• Large logo on back and smaller one on front. should utilize Red, white, and black.
• I am thinking of using a soft touch coating on the card so keep that in mind.
• Contact info should be very easy to read, think older clients.
Nice to have
• I would like to see a design with rounded corners on the card
Should not have
• pictures of homes or other home graphics.

```html
<!DOCTYPE html>
<html lang="en">
<head>
<meta charset="utf-8">
<title>Keystone Home Buyers – Business Card</title>
<link href="https://fonts.googleapis.com/css2?family=Lato:wght@400;700;900&display=swap" rel="stylesheet">
<style>
  :root {
    --brand-red: #ec1f27;
    --brand-black: #000000;
    --brand-white: #ffffff;
    --backdrop: #1d1d1f;
  }
  * { box-sizing: border-box; margin: 0; padding: 0; }
  html, body {
    width: 1200px;
    height: 800px;
    overflow: hidden;
    background: var(--backdrop);
  }
  .sheet {
    width: 1200px;
    height: 800px;
    display: flex;
    align-items: center;
    justify-content: center;
    gap: 40px;
  }
  .card {
    width: 540px;
    height: 315px;
    background: var(--brand-white);
    border-radius: 26px;
    position: relative;
    font-family: "Lato", Arial, sans-serif;
    color: var(--brand-black);
  }
  /* Front side */
  .contact-list {
    list-style: none;
    position: absolute;
    left: 40px;
    top: 30px;
  }
  .contact-line {
    font-size: 34px;
    font-weight: 400;
    line-height: 1;
    padding: 6px 10px 6px 0;
    margin-bottom: 12px;
    display: inline-block;
    border-bottom: 3px solid var(--brand-red);
  }
  .contact-item { display: block; }
  .contact-line--plain { border-bottom: none; }
  .brand-small {
    position: absolute;
    right: 36px;
    bottom: 36px;
    display: flex;
    align-items: center;
    gap: 10px;
  }
  .brand-small .brand-name {
    font-size: 17px;
    font-weight: 900;
    letter-spacing: 1.5px;
    line-height: 1.15;
    text-transform: uppercase;
  }
  .brand-mark {
    background: var(--brand-red);
    flex: none;
  }
  .brand-small .brand-mark { width: 18px; height: 18px; }
  /* Back side */
  .card--back {
    display: flex;
    align-items: center;
    justify-content: center;
  }
  .brand-large {
    display: flex;
    align-items: center;
    gap: 22px;
  }
  .brand-large .brand-mark { width: 44px; height: 44px; }
  .brand-large .brand-name {
    font-size: 46px;
    font-weight: 900;
    letter-spacing: 3px;
    line-height: 1.1;
    text-transform: uppercase;
  }
</style>
</head>
<body>
  <main class="sheet">
    <section class="card card--front" aria-label="Card front">
      <ul class="contact-list">
        <li class="contact-item"><span class="contact-line">Dara Whitfield</span></li>
        <li class="contact-item"><span class="contact-line">Maker &amp; Founder</span></li>
        <li class="contact-item"><span class="contact-line">dara@whitmail.com</span></li>
        <li class="contact-item"><span class="contact-line contact-line--plain">07700 900 418</span></li>
      </ul>
      <div class="brand-small">
        <span class="brand-mark"></span>
        <span class="brand-name">Keystone<br>Home Buyers</span>
      </div>
    </section>
    <section class="card card--back" aria-label="Card back">
      <div class="brand-large">
        <span class="brand-mark"></span>
        <span class="brand-name">Keystone<br>Home Buyers</span>
      </div>
    </section>
  </main>
</body>
</html>
```